Business Card for TKR, logo files already created

Please, can you assist with creating a Business card the TKR graphics which are already listed on www.tarnkeyrelay.example
The business card should be modern and upmarket, textured designs are welcome. Please feel free to express yourself and be very bold with your design.

Target Market(s)

Cyber Security

Industry/Entity Type

Information Technology

Contact Information for Business Card

Company Name
Name
Title
Mobile
Fax or Tel
email
url

Font styles to use
Serif
Sans Serif

Colors
3277b5
85acd3
ffffff

```html
<!DOCTYPE html>
<html lang="en">
<head>
<meta charset="utf-8">
<title>TKR Business Card</title>
<link rel="stylesheet" href="https://fonts.googleapis.com/css2?family=Archivo:wght@400;600;800;900&family=Roboto+Condensed:wght@500;700&display=swap">
<style>
  :root {
    --stage: #5b5b5b;
    --navy: #233f96;
    --blue: #3277b5;
    --sky: #85acd3;
    --white: #ffffff;
    --grey: #6d6d6d;
    --deep: #14254f;
  }
  * { margin: 0; padding: 0; box-sizing: border-box; }
  html, body { width: 1200px; height: 900px; overflow: hidden; }
  body {
    background: var(--stage);
    font-family: "Archivo", sans-serif;
    display: flex;
    flex-direction: column;
    align-items: center;
    justify-content: center;
    gap: 60px;
  }
  .card {
    width: 620px;
    height: 354px;
    border-radius: 26px;
    position: relative;
    overflow: hidden;
    box-shadow: 0 10px 24px rgba(0,0,0,.35);
  }

  /* Back of card */
  .card-back {
    background: radial-gradient(circle at 50% 45%, var(--white) 0%, #dce9f6 16%, var(--sky) 34%, var(--blue) 58%, var(--deep) 100%);
  }
  .card-back .tech-art {
    position: absolute; inset: 0;
    background: radial-gradient(circle at 50% 45%, transparent 30%, rgba(133,172,211,.25) 31%, transparent 33%, transparent 44%, rgba(255,255,255,.18) 45%, transparent 47%);
  }
  .brand-block {
    position: absolute; inset: 0;
    display: flex; flex-direction: column; align-items: center; justify-content: center;
    text-align: center;
  }
  .brand-initials {
    font-weight: 900; font-size: 118px; line-height: .9;
    color: var(--navy); letter-spacing: 2px;
  }
  .brand-name {
    font-weight: 900; font-size: 34px; color: var(--navy);
    letter-spacing: 1px; margin-top: 4px;
  }
  .brand-rule {
    width: 330px; height: 2px; background: var(--grey); margin: 8px 0 6px;
  }
  .tagline {
    font-family: "Roboto Condensed", sans-serif; font-weight: 500;
    font-size: 16px; letter-spacing: 2.4px; color: var(--navy);
  }

  /* Front of card */
  .card-front { background: var(--white); }
  .front-art {
    position: absolute; right: -80px; bottom: -110px;
    width: 340px; height: 340px; border-radius: 50%;
    background: radial-gradient(circle, #f4f8fc 0%, #cfe0f1 22%, var(--sky) 42%, var(--blue) 66%, rgba(50,119,181,.15) 72%, transparent 74%);
  }
  .front-mark {
    position: absolute; right: 62px; bottom: 48px;
    font-weight: 900; font-size: 32px; color: var(--navy);
  }
  .identity { position: absolute; left: 40px; top: 34px; }
  .person-name {
    font-weight: 900; font-size: 58px; line-height: .92;
    color: var(--navy); text-transform: uppercase;
  }
  .person-title {
    font-weight: 400; font-size: 15px; letter-spacing: 11px;
    color: var(--grey); margin-top: 10px;
  }
  .contacts { position: absolute; left: 40px; bottom: 34px; list-style: none; }
  .contacts li {
    display: flex; align-items: center; gap: 9px;
    font-family: "Roboto Condensed", sans-serif; font-weight: 700;
    font-size: 19px; color: var(--navy); line-height: 1.35;
  }
  .contacts svg { width: 14px; height: 14px; fill: var(--grey); flex: none; }
</style>
</head>
<body>

  <section class="card card-back">
    <div class="tech-art" role="img" aria-label="Glowing blue cyber technology circuit rings"></div>
    <div class="brand-block">
      <div class="brand-initials">TKR</div>
      <div class="brand-name">TARNKEY RELAY</div>
      <div class="brand-rule"></div>
      <div class="tagline">SECURE NETWORKS FOR BUSINESS</div>
    </div>
  </section>

  <section class="card card-front">
    <div class="front-art" role="img" aria-label="Blue cyber security rings with a padlock"></div>
    <div class="front-mark">TKR</div>
    <div class="identity">
      <h1 class="person-name">Daniel<br>Morrow</h1>
      <p class="person-title">DIRECTOR</p>
    </div>
    <ul class="contacts">
      <li><svg viewBox="0 0 16 16"><path d="M4 1l3 3-2 2c1 2 3 4 5 5l2-2 3 3-2 3C7 15 1 9 1 3z"/></svg>+1-555-010-4055</li>
      <li><svg viewBox="0 0 16 16"><rect x="4" y="1" width="8" height="4"/><rect x="1" y="6" width="14" height="6" rx="1"/><rect x="4" y="11" width="8" height="4"/></svg>+1-555-010-4044</li>
      <li><svg viewBox="0 0 16 16"><path d="M1 3h14v10H1z M1 3l7 6 7-6" stroke="#fff" stroke-width="1"/></svg>contact@tarnkeyrelay.example</li>
      <li><svg viewBox="0 0 16 16"><circle cx="8" cy="8" r="7"/><path d="M1 8h14M8 1c-3 4-3 10 0 14M8 1c3 4 3 10 0 14" stroke="#fff" fill="none" stroke-width="1"/></svg>www.tarnkeyrelay.example</li>
    </ul>
  </section>

</body>
</html>
```